Banner for promote service of debit card

We are PagaVelo and we need the banners to be posted on the facebook and instagram pages.
We want something to communicate that it is an exclusive debit card full of services.
Low commissions.
Our competitors:
https://www.nortapay-pagos.it/it/home.html
https://www.zelkor-conti.it/it/
https://www.fotoreelz.it/serravanbank/
sendquillo
maybe some banner that makes the idea of a convenient debit card that everyone can use.
Girls enjoying card shopping.
Please check also website for slogans and phrases to use
https://www.pagavelo-carta.it/
Should show the services.
We must convey that it is a fast, simple card that guarantees privacy.
We need strong banners that attract people as these ban will be sponsored on instagram and facebook
Target Market(s)
People 18-35 y
Open Bank account. low commissions. Easy to use. No limits. 100% Privacy.
Requirements
Must have
- Written in Italian.

```html
<!DOCTYPE html>
<html lang="it">
<head>
<meta charset="utf-8">
<title>PagaVelo – Una carta per tutti</title>
<link href="https://fonts.googleapis.com/css2?family=Montserrat:wght@300;400;500;700;800&display=swap" rel="stylesheet">
<style>
  :root {
    --page: #ffffff;
    --sky-light: #4bc4d7;
    --sky-deep: #37abcf;
    --sun: #ffdd1f;
    --navy: #1b3a5c;
    --white: #ffffff;
    --coral: #ff5a3c;
  }
  html, body {
    margin: 0;
    padding: 0;
    width: 1200px;
    height: 1200px;
    overflow: hidden;
    background: var(--page);
    font-family: "Montserrat", sans-serif;
  }
  .banner {
    position: absolute;
    left: 84px;
    top: 330px;
    width: 1032px;
    height: 541px;
    overflow: hidden;
    background: var(--sky-light);
  }
  .banner__backdrop {
    position: absolute;
    inset: 0;
  }
  .hero-photo {
    position: absolute;
    left: 388px;
    top: 18px;
    width: 328px;
    height: 523px;
    border-radius: 150px 150px 0 0;
    background: linear-gradient(180deg, #5a3328 0%, #e8b9a2 30%, #d53a55 52%, #c4234a 100%);
    z-index: 1;
  }
  .headline {
    position: absolute;
    left: 48px;
    top: 54px;
    margin: 0;
    line-height: 1;
    z-index: 2;
  }
  .headline__intro {
    display: block;
    font-weight: 300;
    font-size: 64px;
    color: var(--white);
    text-shadow: 2px 3px 0 var(--navy);
    letter-spacing: -1px;
  }
  .headline__main {
    display: block;
    margin-top: 6px;
    font-weight: 800;
    font-size: 60px;
    line-height: 64px;
    color: var(--sun);
    text-shadow: -3px 4px 0 var(--navy);
    letter-spacing: -1px;
  }
  .claims {
    position: absolute;
    left: 48px;
    top: 278px;
    margin: 0;
    padding: 0;
    list-style: none;
    color: var(--white);
    font-weight: 500;
    font-size: 22px;
    line-height: 31px;
    z-index: 2;
  }
  .privacy-note {
    position: absolute;
    left: 0;
    top: 429px;
    margin: 0;
    width: 342px;
    height: 70px;
    box-sizing: border-box;
    padding: 10px 0 0 48px;
    background: var(--sun);
    border-radius: 0 14px 14px 0;
    color: var(--navy);
    font-size: 13px;
    line-height: 17px;
    text-transform: uppercase;
    z-index: 2;
  }
  .privacy-note strong { font-weight: 800; }
  .privacy-note span { font-weight: 400; }
  .card-visual {
    position: absolute;
    border-radius: 10px;
    box-shadow: 0 6px 14px rgba(0,0,0,0.18);
    z-index: 2;
  }
  .card-visual--back {
    left: 694px;
    top: 88px;
    width: 240px;
    height: 158px;
    background: linear-gradient(135deg, #ff9d1a 0%, #ffd21f 60%, #ffe63a 100%);
  }
  .card-visual--front {
    left: 740px;
    top: 116px;
    width: 242px;
    height: 160px;
    background: linear-gradient(160deg, #d9a7c0 0%, #e6707a 45%, #d5263d 100%);
  }
  .brand {
    position: absolute;
    left: 760px;
    top: 410px;
    display: flex;
    align-items: center;
    gap: 12px;
    z-index: 2;
  }
  .brand__dot {
    width: 22px;
    height: 22px;
    border-radius: 50%;
    background: var(--coral);
  }
  .brand__name {
    font-weight: 700;
    font-size: 38px;
    color: var(--white);
  }
</style>
</head>
<body>
  <section class="banner">
    <svg class="banner__backdrop" width="1032" height="541" viewBox="0 0 1032 541" aria-hidden="true">
      <polygon points="0,0 40,0 1032,475 1032,541 0,541" fill="var(--sky-deep)"/>
    </svg>

    <div class="hero-photo" role="img" aria-label="Foto di una ragazza sorridente in maglia rossa che porge una carta di debito gialla"></div>

    <h1 class="headline">
      <span class="headline__intro">All in one!</span>
      <span class="headline__main">Una carta<br>per tutti</span>
    </h1>

    <ul class="claims">
      <li>Enjoy your cart!</li>
      <li>Fai quello che vuoi.</li>
      <li>Nessun limite.</li>
      <li>Nessun controllo</li>
    </ul>

    <p class="privacy-note">
      <strong>Dobbiamo comunicare che è</strong><br>
      <span>una carta semplice e veloce che</span><br>
      <strong>garantisce la privacy.</strong>
    </p>

    <div class="card-visual card-visual--back" role="img" aria-label="Illustrazione di una carta di debito gialla"></div>
    <div class="card-visual card-visual--front" role="img" aria-label="Illustrazione di una carta di debito rossa"></div>

    <div class="brand">
      <span class="brand__dot"></span>
      <span class="brand__name">PagaVelo</span>
    </div>
  </section>
</body>
</html>
```